I need to redesign my landing page into a high converting landing page adding 3 new elements

I need to redesign my landing page using all the same content, images etc. on the current page https://www.brightlanepromoworks.biz/travel_agency but also adding three new elements to the new redesign.

Please be sure to use my current header and footer from my current website since I will just plug the new design into it...

The Three New Elements Are Below (add these 3 new elements in addition to the current content)

1. Add a video element with this content:
Watch Below To See How Your Industry Uses Our Incentives To Skyrocket Their Sales!

2. Add the element of the 6 types of incentives they can offer.
You can use the same content and images that we use in this module on the homepage at www.brightlanepromoworks.biz ATTACHED IMAGE BUT YOU CAN FIND THE ORIGINAL IMAGES ON HOMEPAGE

3. Add 1 more call to action to give website visitors two choices:
A. Sign Up For 14 Days Risk Free
OR
B. Book A Live Call

Target Market(s)

Travel agents and travel advisors

Industry/Entity Type

marketing

Requirements
Must have
• HIGH CONVERTING LANDING PAGE
Nice to have
• short and to the point...no fluff

```html
<!DOCTYPE html>
<html lang="en">
<head>
<meta charset="utf-8">
<title>Brightlane Promoworks – Travel Agency Incentives</title>
<link href="https://fonts.googleapis.com/css2?family=Roboto:wght@400;500;700;900&display=swap" rel="stylesheet">
<style>
:root{
  --blue:#1b75bc;
  --navy:#2b2473;
  --band:#2a2676;
  --ink:#222;
  --muted:#6b6b6b;
  --soft:#f4f4f6;
  --white:#fff;
  --line:#d9d9de;
  --card:#f2f2f4;
  --pink:#c26b8a;
}
*{box-sizing:border-box;margin:0;padding:0}
html,body{width:1200px;height:3687px;overflow:hidden}
body{position:relative;font-family:'Roboto',sans-serif;color:var(--ink);background:var(--white)}
.abs{position:absolute}
.center{text-align:center;left:0;width:1200px}

.site-header{top:0;left:0;width:1200px;height:72px;background:var(--white)}
.brand{left:110px;top:16px;display:flex;align-items:center;gap:10px}
.brand-mark{width:30px;height:30px;border-radius:50%;background:var(--blue)}
.brand-name{font-size:22px;font-weight:700;color:var(--blue);letter-spacing:.5px}
.main-nav{right:110px;top:29px;display:flex;gap:27px;font-size:14px;font-weight:500;color:#111}

.hero{top:72px;left:0;width:1200px;height:560px;border-radius:0 0 100px 100px;
  background:linear-gradient(180deg,#c98b6a 0%,#8aa7ad 25%,#3f8a72 45%,#2f9c96 65%,#4fb6a8 85%,#6bc2b0 100%)}
.hero-title{top:180px;font-size:44px;line-height:60px;color:var(--white);font-weight:400;text-transform:uppercase;letter-spacing:-.5px}
.hero-title b{font-weight:900}
.btn{display:inline-block;font-size:13px;font-weight:700;color:var(--white);text-transform:uppercase;border-radius:6px;text-align:center}
.btn-primary{background:var(--blue);line-height:46px}
.btn-outline{border:2px solid var(--white);line-height:42px}

.section-title{font-size:36px;line-height:43px;color:var(--navy);font-weight:500;text-transform:uppercase}
.section-title b{color:var(--blue);font-weight:900}
.card{top:819px;width:230px;height:300px;border-radius:8px;overflow:hidden}
.card-label{position:absolute;bottom:18px;left:0;width:100%;text-align:center;color:var(--white);font-size:16px;font-weight:700;line-height:25px;text-transform:uppercase}
.arrow{width:34px;height:34px}

.promise-band{top:1200px;left:0;width:1200px;height:195px;background:var(--band)}
.promise-band p{position:absolute;top:48px;left:140px;width:920px;text-align:center;color:var(--white);font-size:20px;font-weight:700;line-height:34px}

.lead{font-size:15px;line-height:26px;color:#444}
.ad-panel{left:111px;top:1613px;width:977px;height:366px;border:3px solid var(--line);border-radius:24px}
.ad-label{font-size:9px;line-height:11px;color:#555}
.ad-template{border:1px solid #ddd;box-shadow:0 2px 4px rgba(0,0,0,.15);overflow:hidden;background:var(--card)}
.ad-photo{position:absolute;left:0;right:0;background:linear-gradient(180deg,#8a4a5e 0%,#c26b8a 55%,#e6b3c3 100%)}

.testimonials{top:2135px;left:0;width:1200px;height:475px;background:var(--soft)}
.test-title{top:2177px;font-size:36px;font-weight:500;color:var(--navy)}
.test-title b{color:#111;font-weight:900}
.avatar{border-radius:50%;background:linear-gradient(160deg,#d8d3cf,#8a7a72)}
.dot{border-radius:50%}
.quote-name{top:2350px;font-size:17px;font-weight:700;color:#111}
.quote{top:2385px;left:170px;width:860px;text-align:center;font-size:15px;line-height:25.7px;color:var(--muted)}
.pager{top:2553px;left:576px;display:flex;gap:5px;align-items:center}
.pager span{width:11px;height:11px;border:1.5px solid #555;border-radius:50%}
.pager span.on{width:15px;height:15px;background:var(--blue);border:3px solid #b9d4ea}

.blue-base{top:3120px;left:0;width:1200px;height:567px;background:var(--blue)}
.video{left:111px;top:2700px;width:977px;height:483px;border-radius:24px;overflow:hidden;background:linear-gradient(180deg,#5a514a 0%,#3d3733 55%,#2a2522 100%)}
.video-caption{position:absolute;bottom:36px;left:0;width:100%;text-align:center;color:var(--white);font-size:20px;font-weight:700}

.footer-col h3{font-size:19px;font-weight:700;color:var(--white);text-transform:uppercase;margin-bottom:20px}
.footer-col a{display:block;color:var(--white);font-size:15px;line-height:21.5px;text-decoration:none}
.contact-item{position:absolute;left:0;display:flex;gap:14px}
.contact-icon{width:44px;height:44px;border-radius:50%;background:var(--white);flex:none;display:flex;align-items:center;justify-content:center}
.contact-text{color:var(--white);font-size:15px;line-height:23px}
.contact-text b{font-weight:700;display:block}
.footer-rule{top:3643px;left:111px;width:977px;height:1px;background:rgba(255,255,255,.35)}
.copyright{top:3655px;font-size:15px;color:var(--white)}
</style>
</head>
<body>

<header class="site-header abs">
  <div class="brand abs"><span class="brand-mark"></span><span class="brand-name">BRIGHTLANE PROMOWORKS</span></div>
  <nav class="main-nav abs"><span>HOME</span><span>INCENTIVES LIST</span><span>GET FREE SAMPLES</span><span>INTEGRATIONS</span><span>INDUSTRIES</span></nav>
</header>

<section class="hero abs" role="img" aria-label="Tropical lagoon at sunset with a wooden outrigger boat on clear turquoise water"></section>
<h1 class="hero-title abs center"><b>Imagine being able to</b>&nbsp; offer BOGO<br>deals with <b>every booking!</b></h1>
<a class="btn btn-primary abs" style="left:388px;top:322px;width:239px">Sign up for 14 days risk free</a>
<a class="btn btn-outline abs" style="left:642px;top:322px;width:170px">Book a live call</a>

<h2 class="section-title abs center" style="top:694px"><b>Our marketing incentives</b> can<br>help you with</h2>

<svg class="arrow abs" style="left:39px;top:953px" viewBox="0 0 34 34"><circle cx="17" cy="17" r="17" fill="#111"/><path d="M20 10l-7 7 7 7" stroke="#fff" stroke-width="2.5" fill="none"/></svg>
<svg class="arrow abs" style="left:1124px;top:953px" viewBox="0 0 34 34"><circle cx="17" cy="17" r="16" fill="#fff" stroke="#111" stroke-width="1.5"/><path d="M14 10l7 7-7 7" stroke="#111" stroke-width="2" fill="none"/></svg>

<div class="card abs" style="left:111px;background:linear-gradient(180deg,#9aa0a3,#4a6b74 55%,#1b7f9a)" role="img" aria-label="Swimmer in a turquoise cave lagoon"><div class="card-label">Special promotion<br>giveaway</div></div>
<div class="card abs" style="left:360px;background:linear-gradient(180deg,#2f8a6c,#3bbcc0 45%,#7fd6d4)" role="img" aria-label="Clear shallow tropical water from above"><div class="card-label">Referral gifts</div></div>
<div class="card abs" style="left:609px;background:linear-gradient(180deg,#6f9fd4,#3d6b3f 40%,#7a6a55 70%,#4ea9a8)" role="img" aria-label="Thatched huts on stilts over water"><div class="card-label">Enticement for<br>booking a flight</div></div>
<div class="card abs" style="left:858px;background:linear-gradient(180deg,#3f7fcf,#6d8fb0 45%,#1f5a8a 75%,#2b6f9a)" role="img" aria-label="Small boat moored in a calm bay"><div class="card-label">Gifts for booking<br>a cruise</div></div>

<div class="promise-band abs"><p>Attract More New Customers Giving Away Free Vacation Certificates, Cruise Vouchers, Smart Devices, Dining Takeout Vouchers And More. You’ll Never Pay For A Single Certificate, Vacation or Any Item, Ever.</p></div>

<h2 class="section-title abs center" style="top:1473px"><b>Plug in play</b> packs</h2>
<p class="lead abs center" style="top:1543px">Proven SocialFeed™ Ad Templates, High-Converting Banner Ad Templates To Use With The SearchNet™ Display Network Plus<br>Time-Tested Print Ad Templates That We Provide To You For Free With Your BPW Package.</p>

<div class="ad-panel abs"></div>
<p class="ad-label abs" style="left:198px;top:1641px">Photo Feed<br>1080x1080</p>
<p class="ad-label abs" style="left:365px;top:1641px">Social Feed<br>1200x628</p>
<p class="ad-label abs" style="left:623px;top:1641px">Web Banner and Display Ads<br>300x600</p>
<p class="ad-label abs" style="left:778px;top:1652px">600x600</p>
<div class="ad-template abs" style="left:198px;top:1678px;width:147px;height:268px" role="img" aria-label="Photo feed ad template with a pink suitcase travel offer">
  <div class="ad-photo" style="top:44px;height:150px"></div>
</div>
<div class="ad-template abs" style="left:365px;top:1678px;width:236px;height:268px" role="img" aria-label="Social feed ad template with a pink suitcase travel offer">
  <div class="ad-photo" style="top:72px;height:130px"></div>
</div>
<div class="ad-template abs" style="left:623px;top:1670px;width:137px;height:276px" role="img" aria-label="Tall banner ad template with a pink suitcase travel offer">
  <div class="ad-photo" style="top:0;bottom:0;background:linear-gradient(180deg,#6e3a4c 0%,#b35d7d 50%,#d894ad 100%)"></div>
</div>
<div class="ad-template abs" style="left:778px;top:1678px;width:223px;height:222px" role="img" aria-label="Square print ad template with a pink suitcase travel offer">
  <div class="ad-photo" style="top:0;bottom:0;background:linear-gradient(180deg,#8a4a5e 0%,#c26b8a 60%,#e6b3c3 100%)"></div>
</div>
<p class="ad-label abs" style="left:778px;top:1905px">468x60</p>
<div class="ad-template abs" style="left:778px;top:1920px;width:223px;height:26px" role="img" aria-label="Thin leaderboard banner ad template">
  <div class="ad-photo" style="top:0;bottom:0;background:linear-gradient(90deg,#6e3a4c,#c26b8a 60%,#2b2a66)"></div>
</div>

<svg class="arrow abs" style="left:39px;top:1764px" viewBox="0 0 34 34"><circle cx="17" cy="17" r="17" fill="#111"/><path d="M20 10l-7 7 7 7" stroke="#fff" stroke-width="2.5" fill="none"/></svg>
<svg class="arrow abs" style="left:1124px;top:1764px" viewBox="0 0 34 34"><circle cx="17" cy="17" r="16" fill="#fff" stroke="#111" stroke-width="1.5"/><path d="M14 10l7 7-7 7" stroke="#111" stroke-width="2" fill="none"/></svg>
<a class="btn btn-primary abs" style="left:480px;top:2003px;width:239px">Sign up for 14 days risk free</a>

<section class="testimonials abs"></section>
<h2 class="test-title abs center"><b>CLIENT</b> TESTIMONIALS</h2>
<span class="dot abs" style="left:143px;top:2219px;width:7px;height:7px;background:#29a3e0"></span>
<span class="dot abs" style="left:910px;top:2172px;width:10px;height:10px;background:#f28c1e"></span>
<span class="dot abs" style="left:1069px;top:2236px;width:10px;height:10px;background:var(--navy)"></span>
<span class="dot abs" style="left:329px;top:2322px;width:10px;height:10px;background:var(--navy)"></span>
<span class="avatar abs" style="left:142px;top:2300px;width:48px;height:48px" role="img" aria-label="Client portrait"></span>
<span class="avatar abs" style="left:957px;top:2220px;width:48px;height:48px" role="img" aria-label="Client portrait"></span>
<span class="avatar abs" style="left:556px;top:2242px;width:90px;height:90px" role="img" aria-label="Portrait of the reviewing client"></span>
<p class="quote-name abs center">DANA M.</p>
<p class="quote abs">I have been using BPW for 6 months and have been so impressed with this company. I have used the incentives with my customers to encourage repeat business and referrals. It has always been a pleasure to work with my consultant, Jordan. He calls me by name when we talk on the phone, and treats me like a professional and a friend. I have had several clients redeem their incentives, and all were incredibly pleased with them. Redemption is easy and fast. This strengthens my belief in BPW, and assures that I will use their services for a long time! I would reccomend BPW to all my business associates, and anyone who needs an incentive program to take their business to the next level.</p>
<div class="pager abs"><span></span><span class="on"></span><span></span></div>

<div class="blue-base abs"></div>
<div class="video abs" role="img" aria-label="Video still of a presenter speaking to camera">
  <svg class="abs" style="left:458px;top:212px" width="60" height="60" viewBox="0 0 60 60"><circle cx="30" cy="30" r="30" fill="#1b75bc"/><path d="M24 19l18 11-18 11z" fill="#fff"/></svg>
  <div class="video-caption">Watch Below To See How Your Industry Uses Our Incentives To Skyrocket Their Sales!</div>
</div>
<svg class="arrow abs" style="left:39px;top:2903px" viewBox="0 0 34 34"><circle cx="17" cy="17" r="17" fill="#111"/><path d="M20 10l-7 7 7 7" stroke="#fff" stroke-width="2.5" fill="none"/></svg>
<svg class="arrow abs" style="left:1124px;top:2903px" viewBox="0 0 34 34"><circle cx="17" cy="17" r="16" fill="#fff" stroke="#111" stroke-width="1.5"/><path d="M14 10l7 7-7 7" stroke="#111" stroke-width="2" fill="none"/></svg>

<footer>
  <div class="footer-col abs" style="left:188px;top:3252px">
    <h3>Quick links</h3>
    <a>Home</a><a>The Incentives</a><a>Login</a><a>Sign Up</a><a>Affiliate</a><a>Integrations</a><a>Testimonials</a><a>Faq</a>
    <a style="margin-top:4px;line-height:18px">BPW Distribute Certificate<br>Demo Videos</a>
    <a style="margin-top:6px;line-height:18px">White Label Agency<br>Program</a>
  </div>
  <div class="footer-col abs" style="left:418px;top:3240px;width:360px">
    <h3>Contact us</h3>
    <div class="contact-item" style="top:44px"><span class="contact-icon"><svg width="20" height="20" viewBox="0 0 24 24"><path d="M6.6 10.8a15 15 0 006.6 6.6l2.2-2.2a1 1 0 011-.25 11.4 11.4 0 003.6.57 1 1 0 011 1V20a1 1 0 01-1 1A17 17 0 013 4a1 1 0 011-1h3.5a1 1 0 011 1c0 1.25.2 2.45.57 3.6a1 1 0 01-.25 1z" fill="#1b75bc"/></svg></span>
      <p class="contact-text"><b>PHONE NO:</b>New Sales 1-555-014-2231<br>Current/Past Clients 1-555-014-7780</p></div>
    <div class="contact-item" style="top:141px"><span class="contact-icon"><svg width="20" height="20" viewBox="0 0 24 24"><path d="M3 6h18v12H3z" fill="#1b75bc"/><path d="M3 6l9 7 9-7" stroke="#fff" stroke-width="1.6" fill="none"/></svg></span>
      <p class="contact-text"><b>EMAIL:</b>support@brightlanepromo<br>works.biz</p></div>
    <div class="contact-item" style="top:232px"><span class="contact-icon"><svg width="20" height="22" viewBox="0 0 24 24"><path d="M12 2a7 7 0 00-7 7c0 5 7 13 7 13s7-8 7-13a7 7 0 00-7-7zm0 9.5A2.5 2.5 0 1112 6.5a2.5 2.5 0 010 5z" fill="#1b75bc"/></svg></span>
      <p class="contact-text"><b>LOCATION:</b>420 Harbor View Rd #12<br>Seacliff, CA 90000</p></div>
    <div class="contact-item" style="top:323px"><span class="contact-icon"><svg width="22" height="22" viewBox="0 0 24 24"><circle cx="12" cy="12" r="9" stroke="#1b75bc" stroke-width="2" fill="none"/><path d="M12 7v5l3 2" stroke="#1b75bc" stroke-width="2" fill="none"/></svg></span>
      <p class="contact-text"><b>SMS, EMAIL &amp; ONLINE SUPPORT:</b>MONDAY - FRIDAY 8AM - 5PM PST SAT<br>/SUN/HOLIDAYS CLOSED</p></div>
  </div>
  <div class="footer-col abs" style="left:806px;top:3252px;width:230px">
    <h3>Other links</h3>
    <a style="line-height:25px">Hoteliers</a><a style="line-height:25px">BPW Certificates List</a><a style="line-height:25px">How To Use BPW Certificates</a><a style="line-height:25px">Pop Ups &amp; Sticky Bars</a><a style="line-height:25px">Whitepaper - Increase Sales</a>
    <a style="line-height:18px;margin-top:6px">Whitepaper - Improve Sales<br>During Strange Times</a>
    <a style="line-height:18px;margin-top:8px">Whitepaper - Boost Website<br>Conversions</a>
  </div>
  <div class="footer-rule abs"></div>
  <p class="copyright abs center">© 2024 Brightlane Promoworks Group, Inc. All Rights Reserved.</p>
</footer>

</body>
</html>
```